Quality winery located in Northern California desires wine bottle label redesign

We want to redesign our Drifting Moth brand label. We have been making this wine for 24 years, it is our popular priced point wine ($15.00 a bottle). We would like to see a drifting moth as part of the label motif. Refer to our website to view the current version and the explanation of the name Drifting Moth as seen on the back label. The winemakers name is Bartholomew Ignatius Crane, the website is www.cranecellarsx.example.
We are looking for a front label only, back will remain basically the same.
Updates

Reason: We just havn't reached a consensus yet.

Reason: We have had very few responses from distributors, we would like to have more feedback.

Reason: Apologize for another extension, we still have not heard back from many of our distributors, will contact them this week.

We wanted to thank everyone for investing time and thought into our label design project. This has been a pleasure working with pixel huddle.

Target Market(s)

Buying age 21 -45, buyers of wines in the retail market. Has to stand out on the shelf.

Colors

Designer to choose colors to be used in the design.

Requirements
Must have
• Drifting Moth displayed
Should not have
• Varietal cannot be in script, must be in block letters.

```html
<!DOCTYPE html>
<html lang="en">
<head>
<meta charset="utf-8">
<title>Drifting Moth Chardonnay – Front Label</title>
<link rel="stylesheet" href="https://fonts.googleapis.com/css2?family=Great+Vibes&family=Questrial&family=Cutive+Mono&display=swap">
<style>
  :root {
    --canvas: #ffffff;
    --gold-deep: #a8741e;
    --gold-mid: #c89535;
    --gold-light: #f7e9a0;
    --gold-pale: #fff3b0;
    --gold-script: #d8b463;
    --blue-edge: #1b3550;
    --blue-mid: #1d64a3;
    --blue-core: #2070b2;
    --blue-line: #5aa6e0;
    --label-ink: #e8f0f7;
    --varietal-ink: #111111;
  }
  html, body {
    margin: 0;
    width: 1200px;
    height: 900px;
    overflow: hidden;
    background: var(--canvas);
  }
  .label-canvas { display: block; width: 1200px; height: 900px; }
  .producer-line {
    font-family: "Questrial", sans-serif;
    font-size: 11px;
    letter-spacing: 0.5px;
    fill: var(--label-ink);
  }
  .brand-name {
    font-family: "Great Vibes", cursive;
    font-size: 108px;
    fill: var(--gold-script);
  }
  .varietal {
    font-family: "Questrial", sans-serif;
    font-size: 40px;
    letter-spacing: 2px;
    fill: var(--varietal-ink);
  }
  .appellation {
    font-family: "Cutive Mono", monospace;
    font-size: 27px;
    letter-spacing: 5px;
    fill: var(--label-ink);
  }
  .alcohol-statement {
    font-family: "Cutive Mono", monospace;
    font-size: 17px;
    letter-spacing: 2px;
    fill: var(--label-ink);
  }
</style>
</head>
<body>
<svg class="label-canvas" viewBox="0 0 1200 900" xmlns="http://www.w3.org/2000/svg" role="img" aria-label="Drifting Moth Chardonnay front label">
  <defs>
    <linearGradient id="gold-rim" x1="0" y1="0" x2="1" y2="0">
      <stop offset="0" style="stop-color:var(--gold-deep)"/>
      <stop offset="0.25" style="stop-color:var(--gold-light)"/>
      <stop offset="0.5" style="stop-color:var(--gold-mid)"/>
      <stop offset="0.75" style="stop-color:var(--gold-pale)"/>
      <stop offset="1" style="stop-color:var(--gold-deep)"/>
    </linearGradient>
    <linearGradient id="blue-field" x1="0" y1="0" x2="1" y2="0">
      <stop offset="0" style="stop-color:var(--blue-edge)"/>
      <stop offset="0.28" style="stop-color:var(--blue-mid)"/>
      <stop offset="0.5" style="stop-color:var(--blue-core)"/>
      <stop offset="0.72" style="stop-color:var(--blue-mid)"/>
      <stop offset="1" style="stop-color:var(--blue-edge)"/>
    </linearGradient>
    <linearGradient id="varietal-band" x1="0" y1="0" x2="1" y2="0">
      <stop offset="0" style="stop-color:var(--gold-deep)"/>
      <stop offset="0.35" style="stop-color:var(--gold-light)"/>
      <stop offset="0.7" style="stop-color:var(--gold-pale)"/>
      <stop offset="1" style="stop-color:var(--gold-light)"/>
    </linearGradient>
    <path id="alcohol-arc" d="M 400 605 Q 600 670 800 605"/>
  </defs>

  <g class="label">
    <ellipse class="label-rim" cx="600" cy="450" rx="345" ry="228" fill="url(#gold-rim)"/>
    <ellipse class="label-field" cx="600" cy="450" rx="331" ry="214" fill="url(#blue-field)"/>
    <ellipse class="label-inner-line" cx="600" cy="450" rx="333" ry="216" fill="none" stroke="var(--blue-line)" stroke-width="2"/>

    <rect class="crest-ornament" x="538" y="276" width="124" height="24" rx="10" fill="var(--label-ink)" opacity="0.85" role="img" aria-label="Small white floral crest ornament"/>

    <text class="producer-line" x="397" y="342">BRAM HOLLOWAY'S</text>
    <text class="brand-name" x="600" y="438" text-anchor="middle">Drifting Moth</text>

    <ellipse class="varietal-band" cx="600" cy="511" rx="205" ry="32" fill="url(#varietal-band)"/>
    <text class="varietal" x="600" y="525" text-anchor="middle">CHARDONNAY</text>

    <text class="appellation" x="600" y="597" text-anchor="middle">MENDICINO COUNTY</text>
    <rect class="wave-ornament" x="528" y="608" width="144" height="8" rx="4" fill="var(--label-ink)" opacity="0.6" role="img" aria-label="Thin white wave flourish"/>

    <text class="alcohol-statement"><textPath href="#alcohol-arc" startOffset="50%" text-anchor="middle">ALCOHOL 13.5% BY VOLUME</textPath></text>
  </g>
</svg>
</body>
</html>
```